Health and wellnes company needs business cards

We are a Health and wellness business just relocated to Spain. Here nobody knows our business so we would like to put some of our services on the card. Clean design with logo.

Contact Information for Business Card

Brightmeadow
Clara & Tobias Wennberg
Calle de los Almendros 17
Puerto Alameda
Mobile: 0046 731 402768
info@brightmeadow-example.se

Font styles to use
Serif

Colors
85cae6
85acd3
b768aa

Requirements
Must have
• these Services somewhere on the card
• - Private or group yoga
• - Reconnective healing
• - Kitesurfing lessons
• - Massage
• LOgo somewhere
Nice to have
• Colours that go with the logo please

```html
<!DOCTYPE html>
<html lang="en">
<head>
<meta charset="utf-8">
<title>Brightmeadow business cards</title>
<link rel="stylesheet" href="https://fonts.googleapis.com/css2?family=Marcellus&family=Lora:wght@700&family=Mulish:wght@500&family=Montserrat:wght@400&display=swap">
<style>
  :root {
    --page: #e9ecee;
    --card-white: #ffffff;
    --teal: #6cc4c6;
    --navy: #1b3a64;
    --text-light: #ffffff;
  }
  * { box-sizing: border-box; margin: 0; padding: 0; }
  html, body { width: 1200px; height: 912px; overflow: hidden; }
  body { background: var(--page); position: relative; }

  .card {
    position: absolute;
    width: 560px;
    height: 350px;
    border-radius: 22px;
    overflow: hidden;
    box-shadow: 0 10px 28px rgba(0,0,0,0.15);
  }

  /* Front */
  .card--front { left: 120px; top: 70px; background: var(--card-white); }
  .brand {
    position: absolute;
    left: 0; right: 0; top: 118px;
    display: flex; align-items: center; justify-content: center; gap: 14px;
  }
  .brand__dot {
    width: 34px; height: 34px; border-radius: 50%;
    background: var(--teal);
  }
  .brand__name {
    font-family: "Marcellus", serif;
    font-size: 44px;
    color: var(--navy);
    letter-spacing: 1px;
  }
  .services {
    position: absolute;
    left: 0; right: 0; bottom: 42px;
    text-align: center;
    font-family: "Mulish", sans-serif;
    font-weight: 500;
    font-size: 14.5px;
    color: var(--navy);
    white-space: nowrap;
  }
  .services__sep { color: var(--teal); margin: 0 5px; }

  /* Back */
  .card--back { left: 520px; top: 480px; background: var(--teal); }
  .back__circle {
    position: absolute;
    left: 290px; top: -40px;
    width: 330px; height: 330px;
    border-radius: 50%;
    background: var(--card-white);
  }
  .contact {
    position: absolute;
    left: 46px; top: 112px;
    color: var(--text-light);
    font-family: "Montserrat", sans-serif;
    font-size: 15px;
    line-height: 1.25;
  }
  .contact__names {
    font-family: "Lora", serif;
    font-weight: 700;
    font-size: 17px;
    margin-bottom: 22px;
  }
  .contact__address { margin-left: 26px; margin-bottom: 18px; }
  .contact__lines { list-style: none; margin-left: 26px; }
  .contact__lines li { display: flex; align-items: center; gap: 9px; height: 20px; }
  .contact__lines svg { width: 12px; height: 12px; flex: none; margin-left: -21px; }
</style>
</head>
<body>

  <section class="card card--front">
    <div class="brand">
      <span class="brand__dot"></span>
      <span class="brand__name">BRIGHTMEADOW</span>
    </div>
    <p class="services">
      Private or group yoga<span class="services__sep">•</span>Reconnective healing<span class="services__sep">•</span>Kitesurfing lessons<span class="services__sep">•</span>Massage
    </p>
  </section>

  <section class="card card--back">
    <div class="back__circle"></div>
    <div class="contact">
      <p class="contact__names">Clara &amp; Tobias Wennberg</p>
      <p class="contact__address">Calle de los Almendros 17<br>Puerto Alameda</p>
      <ul class="contact__lines">
        <li>
          <svg viewBox="0 0 12 12" aria-hidden="true"><rect x="3" y="0.5" width="6" height="11" rx="1.2" fill="none" stroke="#fff" stroke-width="1.2"/><circle cx="6" cy="9.6" r="0.7" fill="#fff"/></svg>
          <span>0046 731 402768</span>
        </li>
        <li>
          <svg viewBox="0 0 12 12" aria-hidden="true"><rect x="0.5" y="2" width="11" height="8" fill="#fff"/><path d="M0.5 2 L6 6.5 L11.5 2" fill="none" stroke="#6cc4c6" stroke-width="1.2"/></svg>
          <span>info@brightmeadow-example.se</span>
        </li>
        <li>
          <svg viewBox="0 0 12 12" aria-hidden="true"><circle cx="6" cy="6" r="5.5" fill="#fff"/><path d="M0.5 6 H11.5 M6 0.5 C3 4 3 8 6 11.5 M6 0.5 C9 4 9 8 6 11.5" fill="none" stroke="#6cc4c6" stroke-width="0.9"/></svg>
          <span>www.brightmeadow-example.se</span>
        </li>
      </ul>
    </div>
  </section>

</body>
</html>
```